Home Remodeler Needs a Website!

Single page (plus contact form) website for small home remodeling company. He's got a few pictures he'd like on the site and needs some basic text. He likes clean, simple designs and is "more traditional" in his stylistic preferences. Most of his business comes from word-of-mouth advertising and so the site is just something he needs for people to feel more comfortable with his business.

Target Market(s)

People who want to remodel their homes

Coding

Coded - Design and coding required

Number of Pages Required

2 page

Requirements
Must have
• Main page to include some or all of the attached images, contact page. Neutral colors. Old domain: brindlecoveabodes.com New domain: qm-holdings.com You can pull text from the old site or update it.
Should not have
• No loud colors/loud visual elements

```html
<!DOCTYPE html>
<html lang="en">
<head>
<meta charset="utf-8">
<title>Brindle Cove Abodes</title>
<link href="https://fonts.googleapis.com/css2?family=Poppins:wght@300;400;500;600;700&display=swap" rel="stylesheet">
<style>
:root{
  --sky:#6fc7e8;
  --tan:#c8946a;
  --ink:#1e1e1e;
  --muted:#7a7a7a;
  --line:#e7e7e7;
  --white:#ffffff;
  --gold:#f2b01e;
  --canvas:#f3f3f3;
}
*{margin:0;padding:0;box-sizing:border-box}
html,body{width:1200px;height:3000px;overflow:hidden;background:var(--canvas);font-family:'Poppins',sans-serif;color:var(--ink)}
.page{position:absolute;left:180px;top:15px;width:840px;height:2970px;background:var(--white);overflow:hidden;box-shadow:0 0 30px rgba(0,0,0,.06)}

/* nav */
.nav{position:absolute;left:0;top:0;width:840px;height:60px}
.brand{position:absolute;left:54px;top:19px;font-weight:600;font-size:16px;line-height:20px;color:var(--sky);letter-spacing:.5px}
.nav-links{position:absolute;left:388px;top:22px;display:flex;gap:37px;font-size:10px;line-height:14px;color:#444}
.btn-pricing{position:absolute;left:692px;top:17px;width:85px;height:25px;border-radius:13px;background:var(--tan);color:var(--white);font-size:10px;display:flex;align-items:center;justify-content:center}

/* hero */
.hero{position:absolute;left:35px;top:66px;width:768px;height:390px;border-radius:30px;overflow:hidden}
.hero-photo{position:absolute;inset:0;background:linear-gradient(100deg,#62788f 0%,#2c4866 40%,#152f4d 100%)}
.hero-floor{position:absolute;left:0;right:0;bottom:0;height:110px;background:linear-gradient(180deg,rgba(40,70,110,0) 0%,#3a5c86 60%,#2f4f78 100%)}
.hero-text{position:absolute;left:0;right:0;text-align:center;color:var(--white)}
.hero-welcome{top:78px;font-size:17px;line-height:22px;font-weight:400}
.hero-title{top:112px;font-size:52px;line-height:56px;font-weight:700;letter-spacing:-.5px;text-shadow:0 2px 6px rgba(0,0,0,.25)}
.hero-sub{top:182px;font-size:12px;line-height:17px;font-weight:300}
.scroll-mouse{position:absolute;left:374px;top:336px;width:20px;height:32px;border:1.5px solid rgba(255,255,255,.85);border-radius:10px}
.scroll-mouse::after{content:"";position:absolute;left:8px;top:7px;width:1.5px;height:8px;background:rgba(255,255,255,.85)}

/* headings */
.section-title{position:absolute;font-size:22px;line-height:28px;font-weight:600;color:var(--ink)}
.rule{position:absolute;height:2px;width:60px;background:var(--tan)}

/* about */
.about-copy{position:absolute;left:80px;top:590px;width:360px;font-size:9.5px;line-height:22.6px;color:#555;white-space:nowrap}
.about-frame{position:absolute;left:490px;top:526px;width:273px;height:190px;background:var(--white);box-shadow:0 4px 18px rgba(0,0,0,.12)}
.about-photo{position:absolute;left:6px;top:10px;width:261px;height:172px;background:linear-gradient(180deg,#9a9590 0%,#6c655d 55%,#3e3a36 100%)}
.tan-block{position:absolute;background:var(--tan)}

/* feature cards */
.card{position:absolute;top:883px;width:194px;height:127px;background:var(--white);box-shadow:0 3px 14px rgba(0,0,0,.09);padding:16px 17px}
.card-head{display:flex;justify-content:space-between;font-size:11px;line-height:14px;font-weight:500;color:var(--ink)}
.card-num{color:var(--tan);font-weight:400}
.card-body{margin-top:9px;font-size:7.5px;line-height:14.5px;color:var(--muted)}

/* band */
.band{position:absolute;left:0;top:1092px;width:840px;height:130px;background:var(--sky)}
.band-title{position:absolute;left:0;right:0;top:47px;text-align:center;color:var(--white);font-size:24px;line-height:30px;font-weight:600}

/* services */
.services{position:absolute;left:69px;top:1341px;width:681px;height:358px}
.svc{position:absolute;display:flex;flex-direction:column;align-items:center;justify-content:center;text-align:center;font-size:8px;font-weight:600;color:#333;line-height:12px;padding:0 14px}
.svc-icon{width:40px;height:38px;background:#f5e7da;border:1.5px solid var(--tan);border-radius:4px;margin-bottom:10px}
.svc-active{background:var(--white);box-shadow:0 4px 16px rgba(0,0,0,.12);border:1px solid #ddd}
.vline{position:absolute;width:1px;background:var(--line)}
.hline{position:absolute;height:1px;background:var(--line)}

/* projects */
.projects{position:absolute;left:0;top:1767px;width:840px;height:558px;background:var(--sky);overflow:hidden}
.proj-title{position:absolute;left:0;right:0;top:48px;text-align:center;color:var(--white);font-size:22px;line-height:28px;font-weight:600}
.filters{position:absolute;left:0;right:0;top:130px;display:flex;justify-content:center;gap:28px;color:var(--white);font-size:11px;line-height:14px;font-weight:300}
.filters .on{text-decoration:underline;font-weight:400}
.proj{position:absolute;width:216px;height:143px;border-radius:10px;overflow:hidden}
.warm-a{background:linear-gradient(180deg,#8a6a42 0%,#4c3520 55%,#1f150c 100%)}
.warm-b{background:linear-gradient(180deg,#5b3a3a 0%,#3a2418 50%,#120c0a 100%)}
.warm-c{background:linear-gradient(180deg,#3d5f86 0%,#6a5b48 50%,#2c241c 100%)}
.proj-overlay{position:absolute;inset:0;background:rgba(40,40,40,.45);display:flex;flex-direction:column;align-items:center;justify-content:center;color:var(--white);font-size:11px;line-height:14px;font-weight:600}
.search-dot{width:26px;height:26px;border-radius:50%;background:var(--tan);margin:0 0 30px;display:flex;align-items:center;justify-content:center}

/* testimonials */
.t-card{position:absolute;top:2459px;width:206px;height:229px;background:var(--white);box-shadow:0 3px 14px rgba(0,0,0,.08);text-align:center}
.avatar{width:56px;height:56px;border-radius:50%;background:linear-gradient(180deg,#c9d3dc,#6f8296);margin:12px auto 0}
.t-name{margin-top:13px;font-size:7px;line-height:10px;color:var(--tan);letter-spacing:.3px}
.t-text{margin:12px auto 0;width:160px;font-size:7.5px;line-height:13px;color:#444}
.stars{margin-top:20px;font-size:13px;line-height:16px;letter-spacing:5px;color:var(--gold)}
.t-arrow{position:absolute;top:2572px;font-size:14px;line-height:16px;color:#333}

/* footer */
.footer{position:absolute;left:0;top:2748px;width:840px;height:222px;background:var(--sky);color:var(--white)}
.f-brand{position:absolute;left:50px;top:45px;font-weight:600;font-size:13px;line-height:18px}
.f-about{position:absolute;left:50px;top:75px;width:150px;font-size:6.5px;line-height:10px;opacity:.9}
.f-col{position:absolute;top:40px}
.f-head{font-size:13px;line-height:18px;font-weight:600;margin-bottom:10px}
.f-list{font-size:7.5px;line-height:14px}
.f-contact{display:flex;align-items:center;gap:8px;font-size:7.5px;line-height:10px;margin-bottom:10px}
.social{display:flex;gap:8px}
.social span{width:11px;height:11px;border-radius:50%;border:1.5px solid var(--white)}
.to-top{position:absolute;left:756px;top:165px;width:29px;height:26px;background:var(--tan);border-radius:3px;display:flex;align-items:center;justify-content:center}
.copyright{position:absolute;left:0;right:0;top:205px;text-align:center;font-size:7px;line-height:10px;opacity:.9}
</style>
</head>
<body>
<div class="page">

  <header class="nav">
    <div class="brand">Brindle Cove Abodes</div>
    <nav class="nav-links"><span>Home</span><span>About</span><span>Services</span><span>Contact Us</span></nav>
    <div class="btn-pricing">Pricing</div>
  </header>

  <section class="hero">
    <div class="hero-photo" role="img" aria-label="Living room interior with blue sofa, yellow and teal cushions, potted plants and a small side table"></div>
    <div class="hero-floor"></div>
    <div class="hero-text hero-welcome">— Welcome —</div>
    <h1 class="hero-text hero-title">Brindle Cove Abodes</h1>
    <p class="hero-text hero-sub">When you want affordable, quality home construction services;<br>think of us to do the job.</p>
    <div class="scroll-mouse"></div>
  </section>

  <section class="about">
    <h2 class="section-title" style="left:80px;top:535px">About Brindle Cove Abodes</h2>
    <div class="rule" style="left:80px;top:570px;width:73px"></div>
    <p class="about-copy">Since 1981 Walter Kinsley has built and remodeled over 400 homes and<br>businesses. Let us be your contractor for the next project you start.<br>When quality, value and personal attention to detail are important<br>With over 20 years experience in residential and commercial<br>construction, you can trust your project to Brindle Cove Abodes.</p>
    <div class="tan-block" style="left:475px;top:515px;width:28px;height:28px"></div>
    <div class="about-frame"><div class="about-photo" role="img" aria-label="Modern dining room with a long table, chairs and large window"></div></div>
    <div class="tan-block" style="left:733px;top:689px;width:44px;height:44px"></div>
  </section>

  <section class="features">
    <h2 class="section-title" style="left:0;right:0;top:812px;text-align:center">"Don't Tinker Around"</h2>
    <div class="rule" style="left:391px;top:849px"></div>
    <article class="card" style="left:83px">
      <div class="card-head"><span>Partnership Building</span><span class="card-num">01</span></div>
      <p class="card-body">I have built my business with a partnership of clients, employees, subcontractors, suppliers and inspectors. Since each project is unique, this partnership brings creative ideas to your home.</p>
    </article>
    <article class="card" style="left:325px">
      <div class="card-head"><span>Hands On</span><span class="card-num">02</span></div>
      <p class="card-body">I have deep "hands on" history in construction from foundations to final finishing touches.</p>
    </article>
    <article class="card" style="left:566px">
      <div class="card-head"><span>Friendly Subcontrators</span><span class="card-num">03</span></div>
      <p class="card-body">Our subcontractors are our friends and will become yours too. When called upon to explain their part of the process, they are glad to.</p>
    </article>
  </section>

  <section class="band">
    <h2 class="band-title">Commercial and Residential Contracting</h2>
  </section>

  <h2 class="section-title" style="left:0;right:0;top:1262px;text-align:center">All In One Package</h2>
  <div class="rule" style="left:393px;top:1302px"></div>

  <section class="services">
    <div class="vline" style="left:156px;top:0;height:358px"></div>
    <div class="vline" style="left:339px;top:0;height:358px"></div>
    <div class="vline" style="left:520px;top:0;height:358px"></div>
    <div class="hline" style="left:0;top:105px;width:681px"></div>
    <div class="hline" style="left:0;top:241px;width:681px"></div>

    <div class="svc" style="left:0;top:0;width:156px;height:105px"><div class="svc-icon" role="img" aria-label="Consultation icon"></div>Pre Construction<br>Consultation</div>
    <div class="svc" style="left:156px;top:0;width:183px;height:105px"><div class="svc-icon" role="img" aria-label="Brick wall icon"></div>New Construction</div>
    <div class="svc" style="left:339px;top:0;width:181px;height:105px"><div class="svc-icon" role="img" aria-label="Kitchen icon"></div>Remodeling / Kitchens And<br>Baths</div>
    <div class="svc" style="left:520px;top:0;width:161px;height:105px"><div class="svc-icon" role="img" aria-label="House addition icon"></div>Additions</div>

    <div class="svc" style="left:0;top:105px;width:156px;height:136px"><div class="svc-icon" role="img" aria-label="Deck stairs icon"></div>Porches And Decks</div>
    <div class="svc svc-active" style="left:156px;top:105px;width:183px;height:136px"><div class="svc-icon" role="img" aria-label="Historic house icon"></div>Specializing In Historic<br>Renovations.</div>
    <div class="svc" style="left:339px;top:105px;width:181px;height:136px"><div class="svc-icon" role="img" aria-label="Roof tiles icon"></div>Providing Services For<br>Roofing</div>
    <div class="svc" style="left:520px;top:105px;width:161px;height:136px"><div class="svc-icon" role="img" aria-label="Window icon"></div>Window Replacement</div>

    <div class="svc" style="left:0;top:241px;width:156px;height:117px"><div class="svc-icon" role="img" aria-label="Electrical plug icon"></div>Electrical</div>
    <div class="svc" style="left:156px;top:241px;width:183px;height:117px"><div class="svc-icon" role="img" aria-label="Plumber and air conditioner icon"></div>Air Conditioning And Plumbing<br>Upgrades</div>
    <div class="svc" style="left:339px;top:241px;width:181px;height:117px"><div class="svc-icon" role="img" aria-label="Paint bucket icon"></div>Painting</div>
    <div class="svc" style="left:520px;top:241px;width:161px;height:117px"><div class="svc-icon" role="img" aria-label="Concrete mixer truck icon"></div>Concrete Work</div>
  </section>

  <section class="projects">
    <h2 class="proj-title">Our Projects</h2>
    <div class="rule" style="left:391px;top:87px"></div>
    <nav class="filters"><span class="on">All</span><span>Bathroom</span><span>Building</span><span>Decor</span><span>Furniture</span><span>Kitchen</span><span>Living</span></nav>
    <div class="proj warm-a" style="left:74px;top:175px" role="img" aria-label="Open living area with polished floor"></div>
    <div class="proj warm-c" style="left:311px;top:175px" role="img" aria-label="Remodeled bathroom">
      <div class="proj-overlay"><div class="search-dot"><svg width="12" height="12" viewBox="0 0 12 12"><circle cx="5" cy="5" r="3.5" fill="none" stroke="#fff" stroke-width="1.5"/><line x1="7.6" y1="7.6" x2="11" y2="11" stroke="#fff" stroke-width="1.5"/></svg></div>Bathroom Remodeling</div>
    </div>
    <div class="proj warm-b" style="left:546px;top:175px" role="img" aria-label="Kitchen with wooden cabinets and bar counter"></div>
    <div class="proj warm-b" style="left:74px;top:345px" role="img" aria-label="Kitchen with wooden cabinets at night"></div>
    <div class="proj warm-c" style="left:311px;top:345px" role="img" aria-label="Kitchen with island and steel fridge"></div>
    <div class="proj warm-a" style="left:546px;top:345px" role="img" aria-label="Living area with glass doors"></div>
  </section>

  <section class="testimonials">
    <h2 class="section-title" style="left:0;right:0;top:2380px;text-align:center">Our Customer Says</h2>
    <div class="t-arrow" style="left:32px">‹</div>
    <div class="t-arrow" style="left:793px">›</div>
    <article class="t-card" style="left:80px">
      <div class="avatar" role="img" aria-label="Customer portrait"></div>
      <div class="t-name">MARCUS BELL</div>
      <p class="t-text">Lorem Ipsum Dolor Sit Amet, Consectetur Adipiscing Elit. Tincidunt Ut Sed Nibh Leo, Sed Purus Dictum Malesuada. Duis Eget Blandit Pharetra In Sagittis Ullamcorper Ultrices Enim.</p>
      <div class="stars">★★★★★</div>
    </article>
    <article class="t-card" style="left:314px">
      <div class="avatar" role="img" aria-label="Customer portrait"></div>
      <div class="t-name">MARCUS BELL</div>
      <p class="t-text">Lorem Ipsum Dolor Sit Amet, Consectetur Adipiscing Elit. Tincidunt Ut Sed Nibh Leo, Sed Purus Dictum Malesuada. Duis Eget Blandit Pharetra In Sagittis Ullamcorper Ultrices Enim.</p>
      <div class="stars">★★★★★</div>
    </article>
    <article class="t-card" style="left:546px">
      <div class="avatar" role="img" aria-label="Customer portrait"></div>
      <div class="t-name">MARCUS BELL</div>
      <p class="t-text">Lorem Ipsum Dolor Sit Amet, Consectetur Adipiscing Elit. Tincidunt Ut Sed Nibh Leo, Sed Purus Dictum Malesuada. Duis Eget Blandit Pharetra In Sagittis Ullamcorper Ultrices Enim.</p>
      <div class="stars">★★★★★</div>
    </article>
  </section>

  <footer class="footer">
    <div class="f-brand">Brindle Cove Abodes</div>
    <p class="f-about">Since 1981 Walter Kinsley has built and remodeled over 400 homes and businesses. Let us be your contractor for the next project you start. When quality, value and personal attention to detail are important</p>
    <div class="f-col" style="left:274px">
      <div class="f-head">Menu</div>
      <div class="f-list">Home<br>About<br>Service<br>Contact Us<br>Pricing</div>
    </div>
    <div class="f-col" style="left:402px">
      <div class="f-head">Services</div>
      <div class="f-list">New Construction<br>Remodeling<br>Additions<br>Porches And Decks<br>Window Replacement<br>Electrical</div>
    </div>
    <div class="f-col" style="left:549px">
      <div class="f-head">Contact us</div>
      <div class="f-contact"><svg width="9" height="9" viewBox="0 0 10 10"><path d="M2 1 L4 1 L5 3.2 L3.8 4.3 Q4.8 6.2 5.7 6.2 L6.8 5 L9 6 L9 8 Q8.5 9 7.5 9 Q1 8.5 1 2.5 Q1 1.3 2 1Z" fill="#fff"/></svg>555-014-2290</div>
      <div class="f-contact"><svg width="10" height="8" viewBox="0 0 10 8"><rect x=".5" y=".5" width="9" height="7" fill="none" stroke="#fff"/><path d="M.5 .5 L5 4.5 L9.5 .5" fill="none" stroke="#fff"/></svg>office@brindlecoveabodes.com</div>
    </div>
    <div class="f-col" style="left:711px">
      <div class="f-head">Follow us</div>
      <div class="social"><span></span><span></span><span></span><span></span></div>
    </div>
    <div class="to-top"><svg width="10" height="7" viewBox="0 0 10 7"><path d="M1 1 L5 5 L9 1" fill="none" stroke="#fff" stroke-width="1.6"/></svg></div>
    <div class="copyright">© copyright 2021 All Rights Reserved Brindle Cove Abodes</div>
  </footer>

</div>
</body>
</html>
```